VELTRIX GROUP
Project: VXG LOGO
VXG LOGO - Trade
VXG LOGO
Use same font as used in my logo
FAISAL NOORi
GENERAL MANAGER
RIYADH
info@veltrixgroup-example.com
VXGROUP VXGROUP
following changes on your design no #158 the logo upper and left side of the letter head company name bottom and left side of the letter haead The business cards are also in the above pattern. waiting for your immediate response. thanks.

```html
<!DOCTYPE html>
<html lang="en">
<head>
<meta charset="utf-8">
<title>Veltrix Group Stationery</title>
<link href="https://fonts.googleapis.com/css2?family=Roboto:wght@400;500;700&display=swap" rel="stylesheet">
<style>
  :root {
    --brand-blue: #1f56c3;
    --brand-blue-deep: #1a48a8;
    --brand-blue-light: #3a7ae0;
    --faint-mark: #dfe6f0;
    --paper: #ffffff;
    --page-bg: #f1f2f4;
    --frame: #c9ced6;
    --ink: #2a2f38;
  }
  * { margin: 0; padding: 0; box-sizing: border-box; }
  html, body { width: 1200px; height: 883px; overflow: hidden; }
  body {
    position: relative;
    background: var(--page-bg);
    font-family: "Roboto", Arial, sans-serif;
    color: var(--ink);
  }

  /* Letterhead */
  .letterhead {
    position: absolute; left: 62px; top: 24px; width: 571px; height: 828px;
    background: var(--paper); border: 1px solid var(--frame);
  }
  .letterhead__mark {
    position: absolute; left: 12px; top: 14px;
    font-weight: 700; font-size: 44px; line-height: 1; color: var(--brand-blue);
    letter-spacing: -1px;
  }
  .letterhead__watermark {
    position: absolute; left: 78px; top: 300px;
    font-weight: 700; font-size: 230px; line-height: 1; color: var(--faint-mark);
    letter-spacing: -6px;
  }
  .letterhead__footer {
    position: absolute; left: 6px; right: 6px; bottom: 14px; height: 28px;
    display: flex; align-items: center; border-bottom: 2px solid var(--brand-blue);
  }
  .letterhead__company {
    background: var(--brand-blue); color: #fff; font-weight: 700; font-size: 13px;
    height: 100%; padding: 0 10px; display: flex; align-items: center; letter-spacing: .5px;
  }
  .letterhead__contacts {
    margin-left: 14px; font-size: 9px; color: var(--brand-blue); white-space: nowrap;
  }
  .letterhead__contacts b { font-weight: 700; margin: 0 4px; }

  /* Business cards */
  .card {
    position: absolute; overflow: hidden; border: 1px solid var(--brand-blue);
  }
  .card--blue { background: radial-gradient(circle at 60% 35%, var(--brand-blue-light), var(--brand-blue-deep) 75%); color: #fff; }
  .card--white { background: var(--paper); color: var(--brand-blue); }
  .card--front-top { left: 648px; top: 24px; width: 245px; height: 403px; }
  .card--back-top { left: 907px; top: 24px; width: 269px; height: 403px; }
  .card--front-bottom { left: 648px; top: 439px; width: 245px; height: 413px; }
  .card--back-bottom { left: 907px; top: 439px; width: 269px; height: 413px; }

  .card__face {
    position: absolute; left: 0; top: 0; transform-origin: top left;
  }
  .card--front-top .card__face { width: 403px; height: 245px; transform: translate(243px,0) rotate(90deg); }
  .card--front-bottom .card__face { width: 413px; height: 245px; transform: translate(243px,0) rotate(90deg); }
  .card--back-top .card__face { width: 403px; height: 269px; transform: translate(267px,0) rotate(90deg); }
  .card--back-bottom .card__face { width: 413px; height: 269px; transform: translate(267px,0) rotate(90deg); }

  .card__mark { position: absolute; left: 12px; top: 10px; font-weight: 700; font-size: 26px; line-height: 1; }
  .card__person { position: absolute; left: 100px; top: 92px; width: 200px; text-align: center; }
  .card__name { font-weight: 500; font-size: 21px; letter-spacing: .5px; }
  .card__title { font-size: 10px; letter-spacing: 1px; margin-top: 3px; }
  .card__company { position: absolute; left: 12px; bottom: 9px; font-weight: 700; font-size: 16px; letter-spacing: .5px; }
  .card__rule { position: absolute; left: 0; right: 0; bottom: 32px; height: 1px; background: currentColor; opacity: .6; }
  .card__phones { position: absolute; left: 165px; bottom: 38px; font-size: 9px; line-height: 1.4; }
  .card__web { position: absolute; right: 12px; top: 140px; font-size: 9px; line-height: 1.4; text-align: right; }

  .card__company--large { font-size: 22px; bottom: 12px; }
  .card__mark--large { left: auto; right: 14px; top: 28px; font-size: 120px; letter-spacing: -4px; }
  .card__city { position: absolute; right: 14px; bottom: 14px; font-size: 10px; }
  .card__city::before {
    content: ""; display: inline-block; width: 6px; height: 6px; border-radius: 50%;
    background: currentColor; margin-right: 5px; vertical-align: middle;
  }
</style>
</head>
<body>

<section class="letterhead">
  <div class="letterhead__mark">VXG</div>
  <div class="letterhead__watermark">VXG</div>
  <footer class="letterhead__footer">
    <div class="letterhead__company">VELTRIX GROUP</div>
    <div class="letterhead__contacts">P 966-100-5555<b>■</b>F 966-100-6666<b>■</b>info@veltrixgroup-example.com<b>■</b>www.veltrixgroup-example.com</div>
  </footer>
</section>

<article class="card card--blue card--front-top">
  <div class="card__face">
    <div class="card__mark">VXG</div>
    <div class="card__person">
      <div class="card__name">FAISAL NOORi</div>
      <div class="card__title">— GENERAL MANAGER —</div>
    </div>
    <div class="card__web">info@veltrixgroup-example.com<br>www.veltrixgroup-example.com</div>
    <div class="card__phones">P 966-100-5555<br>F 966-100-6666</div>
    <div class="card__rule"></div>
    <div class="card__company">VELTRIX GROUP</div>
  </div>
</article>

<article class="card card--blue card--back-top">
  <div class="card__face">
    <div class="card__mark card__mark--large">VXG</div>
    <div class="card__company card__company--large">VELTRIX GROUP</div>
    <div class="card__city">riyadh</div>
  </div>
</article>

<article class="card card--white card--front-bottom">
  <div class="card__face">
    <div class="card__mark">VXG</div>
    <div class="card__person">
      <div class="card__name">FAISAL NOORi</div>
      <div class="card__title">— GENERAL MANAGER —</div>
    </div>
    <div class="card__web">info@veltrixgroup-example.com<br>www.veltrixgroup-example.com</div>
    <div class="card__phones">P 966-100-5555<br>F 966-100-6666</div>
    <div class="card__rule"></div>
    <div class="card__company">VELTRIX GROUP</div>
  </div>
</article>

<article class="card card--white card--back-bottom">
  <div class="card__face">
    <div class="card__mark card__mark--large">VXG</div>
    <div class="card__company card__company--large">VELTRIX GROUP</div>
    <div class="card__city">riyadh</div>
  </div>
</article>

</body>
</html>
```